Create a professional, eye-catching business card design that reflects the values and services of Brookfern Veterinary Hospital. we provide veterinary services and the business card should be a memorable representation of the clinic and align with its branding and mission. our tag line is "Faithful Friends, Forever Cared For"
Use clean, modern typography. Prioritize readability and professionalism. We would like to see designs that use the color blue, as in the logo example. the final design should communicate professionalism and care, with attention to detail.

```html
<!DOCTYPE html>
<html lang="en">
<head>
<meta charset="utf-8">
<title>Brookfern Veterinary Hospital – Business Card</title>
<link href="https://fonts.googleapis.com/css2?family=Lato:wght@400;700;900&display=swap" rel="stylesheet">
<style>
  :root {
    --navy: #1f2f63;
    --white: #ffffff;
    --grey-text: #7a7a7a;
    --grey-line: #c4c4c4;
    --stage: #2b2d31;
  }
  * { box-sizing: border-box; margin: 0; padding: 0; }
  html, body { width: 1200px; height: 952px; overflow: hidden; }
  body {
    background: var(--stage);
    font-family: "Lato", Arial, sans-serif;
    position: relative;
  }
  .card {
    position: absolute;
    width: 560px;
    height: 320px;
    border-radius: 3px;
    box-shadow: 0 14px 30px rgba(0,0,0,.45);
    overflow: hidden;
  }

  /* Back side */
  .card-back {
    left: 580px; top: 120px;
    background: var(--navy);
    color: var(--white);
  }
  .back-brand {
    position: absolute;
    left: 0; right: 0; top: 92px;
    text-align: center;
  }
  .brand-mark {
    display: inline-block;
    width: 30px; height: 30px;
    border: 2px solid currentColor;
    border-radius: 50%;
    margin-bottom: 10px;
  }
  .brand-name {
    font-weight: 900;
    text-transform: uppercase;
    line-height: 1.05;
    letter-spacing: .5px;
  }
  .brand-name .big { display: block; font-size: 40px; }
  .brand-name .small { display: block; font-size: 14px; letter-spacing: 1.5px; }
  .tagline-row {
    position: absolute;
    left: 0; right: 0; top: 232px;
    display: flex; align-items: center; gap: 14px;
  }
  .tagline-row .rule { flex: 1; height: 1px; background: var(--white); }
  .tagline {
    font-size: 14px; font-weight: 700;
    text-transform: uppercase; letter-spacing: 1.2px;
    white-space: nowrap;
  }

  /* Front side */
  .card-front {
    left: 60px; top: 520px;
    background: var(--white);
    color: var(--navy);
  }
  .front-accent-grey {
    position: absolute; left: 26px; top: 40px;
    width: 3px; height: 170px; background: var(--grey-line);
  }
  .front-accent-navy {
    position: absolute; left: 180px; right: 0; bottom: 26px;
    height: 5px; background: var(--navy);
  }
  .front-brand {
    position: absolute; left: 52px; top: 70px; width: 210px;
    text-align: center;
  }
  .front-brand .brand-name .big { font-size: 32px; }
  .front-brand .brand-name .small { font-size: 11px; letter-spacing: 1px; }
  .contact {
    position: absolute; left: 292px; top: 62px;
  }
  .person-name {
    font-size: 20px; font-weight: 900;
    text-transform: uppercase; letter-spacing: .5px;
  }
  .person-name .light { font-weight: 400; }
  .person-title { font-size: 13px; color: var(--grey-text); margin-top: 2px; }
  .title-rule { width: 44px; height: 1px; background: var(--grey-text); margin: 10px 0 12px; }
  .contact-list { list-style: none; }
  .contact-list li {
    display: flex; align-items: flex-start; gap: 8px;
    font-size: 12px; color: var(--grey-text);
    line-height: 1.35; margin-bottom: 6px;
  }
  .icon {
    flex: none; width: 16px; height: 16px;
    background: var(--navy); border-radius: 3px;
    display: flex; align-items: center; justify-content: center;
  }
  .icon svg { width: 10px; height: 10px; fill: var(--white); }
</style>
</head>
<body>

<section class="card card-back" aria-label="Business card back">
  <div class="back-brand">
    <span class="brand-mark" aria-hidden="true"></span>
    <div class="brand-name">
      <span class="big">Brookfern</span>
      <span class="small">Veterinary Hospital</span>
    </div>
  </div>
  <div class="tagline-row">
    <span class="rule"></span>
    <span class="tagline">Faithful Friends, Forever Cared For</span>
    <span class="rule"></span>
  </div>
</section>

<section class="card card-front" aria-label="Business card front">
  <span class="front-accent-grey"></span>
  <span class="front-accent-navy"></span>

  <div class="front-brand">
    <span class="brand-mark" aria-hidden="true"></span>
    <div class="brand-name">
      <span class="big">Brookfern</span>
      <span class="small">Veterinary Hospital</span>
    </div>
  </div>

  <div class="contact">
    <h1 class="person-name"><span class="light">Daniel M.</span> Whitford</h1>
    <p class="person-title">Managing Director</p>
    <div class="title-rule"></div>
    <ul class="contact-list">
      <li>
        <span class="icon"><svg viewBox="0 0 10 10"><path d="M5 0.5a3.3 3.3 0 0 0-3.3 3.3C1.7 6.3 5 9.5 5 9.5s3.3-3.2 3.3-5.7A3.3 3.3 0 0 0 5 .5zm0 4.7a1.3 1.3 0 1 1 0-2.6 1.3 1.3 0 0 1 0 2.6z"/></svg></span>
        <span>2174 Elmstone Avenue<br>Portland, OR 97205</span>
      </li>
      <li>
        <span class="icon"><svg viewBox="0 0 10 10"><path d="M2.2.8l1.5 1.9-.9 1.1c.6 1.3 1.6 2.3 2.9 2.9l1.1-.9 1.9 1.5-.8 1.6C4.6 8.6 1.4 5.4 0.6 1.6z"/></svg></span>
        <span>+00 987 654 32</span>
      </li>
      <li>
        <span class="icon"><svg viewBox="0 0 10 10"><path d="M.5 2h9v6h-9zM1.2 2.6L5 5.5l3.8-2.9v-.1H1.2z"/></svg></span>
        <span>hello@brookfernvet.com</span>
      </li>
      <li>
        <span class="icon"><svg viewBox="0 0 10 10"><path d="M1 9L9 1M4 1h5v5" stroke="#fff" stroke-width="1.6" fill="none"/></svg></span>
        <span>www.brookfernvet.com</span>
      </li>
    </ul>
  </div>
</section>

</body>
</html>
```